Summit Builders Web Site / Business Cards

Construction Company that specializes in Water and Fire Damage, Residential ReModels, Landscaping and Building ADU (Accessory Dwelling Unit)

Growing and changing families often need additional space, and a remodeling project can often provide that. Adding a new area, or repurposing an existing one can satisfy this requirement.

Other times, homeowners want to update the look in their kitchen or bathroom with more than just a change of cabinetry or vanity doors and drawers. Whatever your needs are, Summit Builders has skilled workers who are bonded and insured, and ready to make your dreams and visions a reality.

Target Market(s)

Home Owners

Industry/Entity Type

Construction Company

Contact Information for Business Card

Center Logo with our information on the corners

Back side to be Logo Only
Contact Info
CSLB License # 4829516
info@summitbuildersca.example
www.summitbuildersca.example

Coding

Coded - Design and coding required

Number of Pages Required

5+ page

Font styles to use
Serif
Sans Serif

Requirements
Must have
• Using our Logo Colors
Home
About Us
Services
Projects / Portfolio
Contact Us
Nice to have
• Colors matching our Logo
Should not have
• Black because it doesnt match our logo

```html
<!DOCTYPE html>
<html lang="en">
<head>
<meta charset="utf-8">
<title>Summit Builders</title>
<link href="https://fonts.googleapis.com/css2?family=Poppins:wght@400;500;600;700&family=Montserrat:wght@400;500;600;700&display=swap" rel="stylesheet">
<style>
:root{
  --orange:#f26b1d;
  --orange-soft:#f58a3f;
  --navy:#1e2140;
  --navy-2:#272a47;
  --ink:#222;
  --muted:#777;
  --light:#f1f1f4;
  --white:#fff;
}
*{box-sizing:border-box;margin:0;padding:0}
html,body{width:1200px;height:5314px;overflow:hidden}
body{font-family:"Montserrat",sans-serif;color:var(--ink);background:var(--white);position:relative}
.abs{position:absolute}
h1,h2,h3,h4{font-family:"Poppins",sans-serif}
.brand{font-family:"Poppins",sans-serif;font-weight:700;letter-spacing:2px;display:flex;align-items:center;gap:10px}
.brand i{display:block;width:18px;height:18px;background:var(--orange)}
/* top bar */
.topbar{left:0;top:0;width:1200px;height:42px;background:var(--navy);color:#cfd0dc;font-size:11px}
.topbar .addr{left:85px;top:14px}
.topbar .addr::before{content:"";display:inline-block;width:7px;height:7px;border-radius:50%;background:var(--orange);margin-right:8px}
.cert{left:856px;top:13px;width:90px;height:16px;background:var(--orange);border-radius:2px}
.socials{display:flex;gap:14px}
.socials span{width:12px;height:12px;border-radius:50%;background:#cfd0dc;display:block}
.topbar .socials{left:978px;top:15px}
/* header */
.header{left:0;top:42px;width:1200px;height:140px;background:var(--white)}
.header .call{left:85px;top:52px;font-size:12px}
.header .call small,.header .mail small{color:var(--orange);display:block;font-size:11px;margin-bottom:3px}
.header .call b,.header .mail b{font-size:12px;font-weight:700}
.header .mail{right:85px;top:52px;text-align:right}
.header .logo{left:0;width:1200px;top:48px;justify-content:center;font-size:30px;color:var(--navy)}
.ico-line{stroke:var(--orange);fill:none;stroke-width:2}
/* nav */
.hero{left:0;top:182px;width:1200px;height:651px;background:linear-gradient(135deg,#6b5a4b,#3b3a44 55%,#5d4c40)}
.hero::after{content:"";position:absolute;inset:0;background:rgba(30,33,64,.55)}
.nav{left:85px;top:182px;width:1028px;height:70px;background:var(--navy);z-index:2;display:flex;align-items:center}
.nav .home{width:70px;height:70px;background:var(--orange);display:flex;align-items:center;justify-content:center}
.nav ul{list-style:none;display:flex;gap:40px;margin-left:34px;color:#fff;font-family:"Poppins",sans-serif;font-size:15px;font-weight:500}
.nav .search{margin-left:auto;margin-right:26px}
.nav .quote{width:170px;height:70px;background:#171a33;color:#fff;font-weight:700;font-size:14px;display:flex;align-items:center;justify-content:center;gap:10px;font-family:"Poppins",sans-serif}
.hero-text{left:0;top:430px;width:1200px;text-align:center;color:#fff;z-index:2}
.hero-text .kicker{font-size:25px;letter-spacing:1px;font-weight:500}
.hero-text h1{font-size:62px;font-weight:700;margin-top:8px;line-height:1.2}
.hero-text h1 span{color:var(--orange)}
.hero-text p{font-size:16px;line-height:30px;margin-top:10px}
.hero-btns{display:flex;justify-content:center;gap:16px;margin-top:24px}
.btn{display:inline-block;font-family:"Poppins",sans-serif;font-weight:600;font-size:14px;padding:0 26px;height:42px;line-height:40px;border:2px solid #fff;color:#fff}
.btn.fill{background:var(--orange);border-color:var(--orange)}
/* what we do */
.intro{left:0;top:935px;width:1200px;text-align:center}
.intro .mark{justify-content:center;font-size:20px;color:var(--navy)}
.intro h2{font-size:24px;font-weight:700;line-height:30px;color:var(--ink);margin-top:30px}
.intro h3{font-size:31px;color:var(--orange);font-weight:700;margin-top:10px}
.card{width:306px;height:307px;background:#fff;box-shadow:0 3px 12px rgba(0,0,0,.14);text-align:center;padding-top:34px}
.card .icon{position:relative;width:70px;height:70px;margin:0 auto}
.card .icon::before{content:"";position:absolute;left:30px;top:0;width:60px;height:60px;border-radius:50%;background:#f0f0f0}
.card .icon svg{position:relative}
.card h4{font-size:19px;font-weight:600;margin-top:16px}
.card p{font-size:13px;color:var(--muted);line-height:21px;margin:10px 34px 0}
.more{font-family:"Poppins",sans-serif;font-size:13px;font-weight:600;margin-top:18px;display:flex;align-items:center;justify-content:center;gap:10px}
.more::before{content:"";width:14px;height:14px;border-radius:50%;background:var(--orange)}
/* about */
.about{left:0;top:1938px;width:1200px;height:767px;background:var(--light)}
.about .shade{left:85px;top:2060px;width:343px;height:322px;background:var(--orange)}
.ph{display:block}
.about .kicker{left:621px;top:2075px;font-size:14px;color:var(--orange)}
.about h2{left:621px;top:2098px;font-size:40px;line-height:48px;font-weight:700;color:var(--ink)}
.about h2 span{color:var(--orange)}
.about p{left:621px;top:2220px;width:490px;font-size:13px;line-height:21px;color:var(--muted)}
.feat{display:flex;align-items:center;gap:22px;font-family:"Poppins",sans-serif;font-weight:700;font-size:14px;line-height:20px}
.feat .c{width:70px;height:70px;border-radius:50%;background:var(--orange);display:flex;align-items:center;justify-content:center}
/* projects */
.proj-bg{left:0;top:2705px;width:1200px;height:318px;background:linear-gradient(90deg,var(--orange),#f5823a)}
.proj-head{left:0;top:2765px;width:1200px;text-align:center;color:#fff}
.proj-head small{font-size:14px;letter-spacing:.5px}
.proj-head h2{font-size:38px;font-weight:700;margin-top:4px}
.pcard{width:325px;height:322px;background:#fff;box-shadow:0 3px 10px rgba(0,0,0,.14)}
.pcard .ph{width:325px;height:246px}
.pcard .tag{position:absolute;left:25px;top:232px;background:var(--orange);color:#fff;font-size:12px;padding:6px 12px}
.pcard h4{position:absolute;left:26px;top:276px;font-size:16px;font-weight:700}
.outline-btn{left:495px;top:3634px;width:210px;height:44px;border:2px solid var(--orange);color:var(--orange);font-family:"Poppins",sans-serif;font-weight:600;font-size:14px;display:flex;align-items:center;justify-content:center;letter-spacing:.5px}
/* stats */
.stats{left:0;top:3760px;width:1200px;display:flex}
.stat{width:264px;text-align:center}
.stat:first-child{margin-left:72px}
.stat b{display:block;font-family:"Poppins",sans-serif;font-size:44px;color:var(--orange);font-weight:500;line-height:50px}
.stat span{font-size:15px;letter-spacing:.5px;color:#333}
/* testimonials */
.testi{left:0;top:3883px;width:1200px;height:645px;background:linear-gradient(180deg,#2b2e4b,var(--navy))}
.testi-head{left:0;top:3950px;width:1200px;text-align:center;color:#fff}
.testi-head small{color:var(--orange);font-size:14px}
.testi-head h2{font-size:38px;font-weight:700;margin-top:4px}
.quote{width:486px;height:188px;border:1px solid #4a4d6b;background:rgba(255,255,255,.04);color:#d6d7e2;font-size:13px;line-height:22px;padding:44px 110px 0 26px}
.quote svg{position:absolute;right:22px;top:38px}
.person{display:flex;align-items:center;gap:22px}
.person .av{width:96px;height:96px;border-radius:50%;background:linear-gradient(135deg,#d9c8b8,#9a8778);border:5px solid #fff}
.person b{display:block;color:var(--orange);font-family:"Poppins",sans-serif;font-size:20px;font-weight:600}
.person span{color:#aeb0c3;font-size:13px}
.dots{left:494px;top:4463px;display:flex;gap:12px}
.dots span{width:44px;height:5px;background:#fff}
.dots span:first-child{background:var(--orange)}
/* cta + footer */
.footer{left:0;top:4693px;width:1200px;height:621px;background:var(--navy)}
.footer-panel{left:790px;top:4693px;width:410px;height:621px;background:#181a33}
.cta{left:85px;top:4573px;width:1028px;height:192px;background:var(--orange);overflow:hidden}
.cta .ph{position:absolute;left:0;top:0;width:400px;height:192px;clip-path:polygon(0 0,100% 0,84% 100%,0 100%)}
.cta h3{position:absolute;left:460px;top:30px;color:#fff;font-size:27px;line-height:34px;font-weight:700;letter-spacing:1px}
.cta .btn{position:absolute;left:460px;top:130px;height:42px;font-size:14px}
.foot-logo{left:85px;top:4870px;color:#fff;font-size:30px}
.foot-about{left:85px;top:4990px;width:260px;color:#d6d7e2;font-size:13px;line-height:21px}
.foot-hours{left:85px;top:5082px;color:#d6d7e2;font-size:13px;line-height:21px}
.foot-hours em{font-style:normal;color:var(--orange)}
.foot-title{color:#fff;font-family:"Poppins",sans-serif;font-size:21px;font-weight:500}
.links{list-style:none;color:#d6d7e2;font-size:13px;line-height:17px;border-left:1px solid #4a4d6b;padding-left:0}
.links li{position:relative;padding-left:32px;margin-bottom:17px}
.links li::before{content:"";position:absolute;left:10px;top:8px;width:12px;height:1px;background:#8e90a8}
.contact{left:834px;top:4910px;color:#d6d7e2;font-size:13px;line-height:21px}
.contact b{color:var(--orange);font-weight:600}
.contact em{color:var(--orange);font-style:normal}
.copy{left:85px;top:5252px;color:#d6d7e2;font-size:13px}
.footer .rule{left:0;top:5220px;width:1200px;height:1px}
.foot-social{left:978px;top:5256px}
</style>
</head>
<body>

<!-- top bar -->
<div class="abs topbar">
  <div class="abs addr">412 W Harbor Ridge Rd, Costa Verde, CA 92799</div>
  <div class="abs cert" aria-label="certificate badge"></div>
  <div class="abs socials"><span></span><span></span><span></span><span></span><span></span></div>
</div>

<!-- header -->
<div class="abs header">
  <div class="abs call" style="padding-left:42px">
    <svg class="abs" style="left:0;top:4px" width="28" height="28" viewBox="0 0 24 24"><path class="ico-line" d="M5 3h4l2 5-2.5 1.5a11 11 0 0 0 6 6L16 13l5 2v4a2 2 0 0 1-2 2A16 16 0 0 1 3 5a2 2 0 0 1 2-2"/></svg>
    <small>Call us</small><b>+1 555 014 2280</b>
  </div>
  <div class="abs brand logo"><i></i>SUMMIT BUILDERS</div>
  <div class="abs mail" style="padding-right:42px">
    <svg class="abs" style="right:0;top:4px" width="28" height="28" viewBox="0 0 24 24"><rect class="ico-line" x="3" y="6" width="18" height="13"/><path class="ico-line" d="M3 6l9 7 9-7"/></svg>
    <small>Email us now</small><b>info@summitbuildersca.example</b>
  </div>
</div>

<!-- hero -->
<div class="abs hero" role="img" aria-label="Construction workers in hard hats laying bricks on a site"></div>
<nav class="abs nav">
  <div class="home"><svg width="34" height="34" viewBox="0 0 24 24"><path d="M3 11l9-8 9 8M5 9.5V21h14V9.5" stroke="#fff" stroke-width="1.8" fill="none"/></svg></div>
  <ul><li>About Us</li><li>Services</li><li>Projects</li><li>Contact Us</li></ul>
  <svg class="search" width="16" height="16" viewBox="0 0 24 24"><circle cx="10" cy="10" r="7" stroke="#fff" stroke-width="3" fill="none"/><path d="M15 15l6 6" stroke="#fff" stroke-width="3"/></svg>
  <div class="quote">GET A QUOTE <svg width="16" height="12" viewBox="0 0 16 12"><path d="M0 6h14M9 1l5 5-5 5" stroke="var(--orange)" stroke-width="2" fill="none"/></svg></div>
</nav>
<div class="abs hero-text">
  <div class="kicker">WE ARE &nbsp;PROFESSIONAL</div>
  <h1>The Best <span>Choose</span> us</h1>
  <p>Our Company has consistently embraced innovation to provide a superior level of<br>This excellence for our customers.</p>
  <div class="hero-btns"><span class="btn">VIEW MORE</span><span class="btn fill">GET A QUOTE</span></div>
</div>

<!-- what we do -->
<section class="abs intro">
  <div class="brand mark"><i></i>SUMMIT</div>
  <h2>TECHNOLOGY TO TAKE PRODUCTS FROM<br>AN IDEA ALL THE WAY TO THE END CONSUMER.</h2>
  <h3>WHAT WE DO</h3>
</section>

<div class="abs card" style="left:95px;top:1169px">
  <div class="icon"><svg width="60" height="60" viewBox="0 0 60 60"><path class="ico-line" d="M6 30L30 8l24 22M12 25v28h36V25M24 53V36h12v17"/></svg></div>
  <h4>Home Construction</h4>
  <p>Acepteur sintas hae cate sed ipsums cupidates nondui proident sunlt culp qui tempore officia sed ipsum temps eserunt sed ipsum</p>
  <div class="more">Read More</div>
</div>
<div class="abs card" style="left:445px;top:1169px">
  <div class="icon"><svg width="60" height="60" viewBox="0 0 60 60"><rect class="ico-line" x="6" y="10" width="42" height="42"/><path class="ico-line" d="M14 44l28-28M38 12l8 8M14 36v8h8"/></svg></div>
  <h4>Exterior Design</h4>
  <p>Acepteur sintas hae cate sed ipsums cupidates nondui proident sunlt culp qui tempore officia sed ipsum temps eserunt sed ipsum</p>
  <div class="more">Read More</div>
</div>
<div class="abs card" style="left:798px;top:1169px">
  <div class="icon"><svg width="60" height="60" viewBox="0 0 60 60"><path class="ico-line" d="M14 28a12 12 0 0 1 24 0zM10 28h32M16 34h20v18H16zM42 20h14v32H42"/></svg></div>
  <h4>Building Remodeling</h4>
  <p>Acepteur sintas hae cate sed ipsums cupidates nondui proident sunlt culp qui tempore officia sed ipsum temps eserunt sed ipsum</p>
  <div class="more">Read More</div>
</div>
<div class="abs card" style="left:95px;top:1522px">
  <div class="icon"><svg width="60" height="60" viewBox="0 0 60 60"><path class="ico-line" d="M6 28h40v24H6zM6 36h40M6 44h40M18 28v8M32 36v8M18 44v8M36 28v-6l14-14"/></svg></div>
  <h4>Renovation</h4>
  <p>Acepteur sintas hae cate sed ipsums cupidates nondui proident sunlt culp qui tempore officia sed ipsum temps eserunt sed ipsum</p>
  <div class="more">Read More</div>
</div>
<div class="abs card" style="left:445px;top:1522px">
  <div class="icon"><svg width="60" height="60" viewBox="0 0 60 60"><path class="ico-line" d="M18 6h20v14H18zM14 20h28v8H14zM28 28v12M24 40h8v16h-8z"/></svg></div>
  <h4>Interior Design</h4>
  <p>Acepteur sintas hae cate sed ipsums cupidates nondui proident sunlt culp qui tempore officia sed ipsum temps eserunt sed ipsum</p>
  <div class="more">Read More</div>
</div>
<div class="abs card" style="left:798px;top:1522px">
  <div class="icon"><svg width="60" height="60" viewBox="0 0 60 60"><path class="ico-line" d="M8 38a22 22 0 0 1 44 0zM4 38h52v6H4zM24 18v20M36 18v20"/></svg></div>
  <h4>Safety Management</h4>
  <p>Acepteur sintas hae cate sed ipsums cupidates nondui proident sunlt culp qui tempore officia sed ipsum temps eserunt sed ipsum</p>
  <div class="more">Read More</div>
</div>

<!-- about -->
<section class="abs about"></section>
<div class="abs shade"></div>
<div class="abs ph" style="left:99px;top:2050px;width:315px;height:310px;background:linear-gradient(160deg,#7fa7d6,#c9b48a 60%,#7e8f3d)" role="img" aria-label="Engineers in hard hats looking up at a building under construction"></div>
<div class="abs ph" style="left:85px;top:2397px;width:236px;height:192px;background:linear-gradient(135deg,#8a7a68,#c8b79c 50%,#5a5048)" role="img" aria-label="Surveyor in a white hard hat using a level instrument"></div>
<div class="abs ph" style="left:336px;top:2222px;width:208px;height:367px;background:linear-gradient(180deg,#5e8fc7,#b9c7d6 55%,#6d7684)" role="img" aria-label="Modern high-rise building against a blue sky"></div>
<div class="abs kicker" style="left:621px;top:2075px;font-size:14px;color:var(--orange)">WHO WE ARE</div>
<h2 class="abs" style="left:621px;top:2100px;font-size:40px;line-height:48px;font-weight:700">WE <span style="color:var(--orange)">DELIVER</span><br>LANDMARK <span style="color:var(--orange)">PROJECTS</span></h2>
<p class="abs" style="left:621px;top:2220px;width:490px;font-size:13px;line-height:21px;color:var(--muted)">We are rethoric question ran over her cheek When she reached the first hills of the Italic Mountains, she had a last view back on the skyline of her hometown Bookmarksgrove, the headline of Alphabet Village and the sub-line of her own road, the Line Lane.</p>
<div class="abs feat" style="left:621px;top:2357px"><div class="c"><svg width="36" height="36" viewBox="0 0 24 24"><path d="M12 3l2.6 5.3 5.9.9-4.2 4.1 1 5.8L12 16.4 6.7 19.1l1-5.8L3.5 9.2l5.9-.9z" stroke="#fff" stroke-width="1.4" fill="none"/></svg></div><div>WE'VE REPUTION<br>FOR EXCELLENCE</div></div>
<div class="abs feat" style="left:885px;top:2357px"><div class="c"><svg width="36" height="36" viewBox="0 0 24 24"><path d="M2 11l5-5 5 3 5-3 5 5-7 7-3-3-3 3z" stroke="#fff" stroke-width="1.4" fill="none"/></svg></div><div>WE BUILD<br>PARTNERSHIPS</div></div>
<div class="abs feat" style="left:621px;top:2470px"><div class="c"><svg width="36" height="36" viewBox="0 0 24 24"><path d="M12 3l8 3v6c0 5-4 8-8 9-4-1-8-4-8-9V6zM8 12l3 3 5-5" stroke="#fff" stroke-width="1.4" fill="none"/></svg></div><div>GUIDED BY<br>COMMITMENT</div></div>
<div class="abs feat" style="left:885px;top:2470px"><div class="c"><svg width="36" height="36" viewBox="0 0 24 24"><path d="M6 10a6 6 0 0 1 12 0zM4 10h16M8 13h8v3a4 4 0 0 1-8 0zM5 22a7 7 0 0 1 14 0" stroke="#fff" stroke-width="1.4" fill="none"/></svg></div><div>A TEAM OF<br>PROFESSIONALS</div></div>

<!-- projects -->
<div class="abs proj-bg"></div>
<div class="abs proj-head"><small>OUR INDUSTRIES WORK</small><h2>OUR PROJECTS</h2></div>

<div class="abs pcard" style="left:85px;top:2878px"><div class="ph" style="background:linear-gradient(135deg,#b8a48a,#7a6a58)" role="img" aria-label="Workers in safety vests on a building frame"></div><span class="tag">CONSTRUCTION</span><h4>BUILDING &amp; CONSTRUCTION</h4></div>
<div class="abs pcard" style="left:437px;top:2878px"><div class="ph" style="background:linear-gradient(135deg,#e8c21e,#b98a4c)" role="img" aria-label="Yellow hard hat and leather tool belt"></div><span class="tag">FIXING</span><h4>HOME FIXING &amp; SUPPORT</h4></div>
<div class="abs pcard" style="left:788px;top:2878px"><div class="ph" style="background:linear-gradient(180deg,#4f7fc5,#a9756b 60%,#5f8a45)" role="img" aria-label="Two-storey brick family house"></div><span class="tag">RENOVATION</span><h4>RENOVATION &amp; FIXING</h4></div>
<div class="abs pcard" style="left:85px;top:3254px"><div class="ph" style="background:linear-gradient(180deg,#8a93b5,#6a6f82 60%,#d99a5a)" role="img" aria-label="Suburban house at dusk with lit windows"></div><span class="tag">BUILDING</span><h4>BUILDING A SPORTS CITY</h4></div>
<div class="abs pcard" style="left:437px;top:3254px"><div class="ph" style="background:linear-gradient(135deg,#3e3430,#b9b2a8 55%,#5a4a40)" role="img" aria-label="Modern kitchen with dark cabinets and bar stools"></div><span class="tag">KITCHEN DESIGN</span><h4>HOME &amp; KITCHEN DESIGN</h4></div>
<div class="abs pcard" style="left:788px;top:3254px"><div class="ph" style="background:linear-gradient(135deg,#e6e8e4,#9aa89a 55%,#3b3b3b)" role="img" aria-label="Bright living room with large windows and dark sofas"></div><span class="tag">INTERIOR</span><h4>OFFICIAL INTERIOR DESIGN</h4></div>
<div class="abs outline-btn">VIEW ALL PROJECTS</div>

<!-- stats -->
<div class="abs stats">
  <div class="stat"><b>53</b><span>TOTAL PROJECTS</span></div>
  <div class="stat"><b>371</b><span>STAFF MEMBERS</span></div>
  <div class="stat"><b>15</b><span>WORKING IN STATES</span></div>
  <div class="stat"><b>2,600</b><span>HOURS FOR WORK</span></div>
</div>

<!-- testimonials -->
<section class="abs testi"></section>
<div class="abs testi-head"><small>TESTIMONIALS</small><h2>WHAT OUR CLIENTS SAY</h2></div>
<div class="abs quote" style="left:85px;top:4077px">...and for all the wonderful work you and your crew are doing. Our team has nothing but good things to say - we are really fortunate to have found you for this project!
  <svg width="62" height="44" viewBox="0 0 62 44"><path d="M4 4h22v20c0 10-6 16-16 18l-2-6c6-2 8-6 8-10H4zM34 4h22v20c0 10-6 16-16 18l-2-6c6-2 8-6 8-10H34z" fill="var(--orange)"/></svg></div>
<div class="abs quote" style="left:627px;top:4077px">Summit Builders is one of the best general contractors we've worked with. The entire team tactfully delivered a project of exceptional quality while staying on schedule and under budget. We hope to work with Summit again in the near future!
  <svg width="62" height="44" viewBox="0 0 62 44"><path d="M4 4h22v20c0 10-6 16-16 18l-2-6c6-2 8-6 8-10H4zM34 4h22v20c0 10-6 16-16 18l-2-6c6-2 8-6 8-10H34z" fill="var(--orange)"/></svg></div>
<div class="abs person" style="left:112px;top:4309px"><div class="av" role="img" aria-label="Client portrait"></div><div><b>Marcus Reed</b><span>Chairman Reed Holdings</span></div></div>
<div class="abs person" style="left:652px;top:4309px"><div class="av" role="img" aria-label="Client portrait"></div><div><b>Elena Park</b><span>Project Manager</span></div></div>
<div class="abs dots"><span></span><span></span><span></span><span></span></div>

<!-- footer -->
<footer class="abs footer"></footer>
<div class="abs footer-panel"></div>
<div class="abs cta">
  <div class="ph" style="background:linear-gradient(180deg,#e9a860,#8a6a4a 55%,#5d6a3a)" role="img" aria-label="Aerial view of a city neighbourhood at sunset"></div>
  <h3>Summit Builders is one of the best<br>general contractors</h3>
  <span class="btn">BOOK A CONSULTATION</span>
</div>
<div class="abs brand foot-logo"><i></i>SUMMIT</div>
<p class="abs foot-about">We work 7 days a week, every day excluding major holidays. Contact us if you have an emergency, with our Hotline and Contact form.</p>
<div class="abs foot-hours"><em>Monday - Friday</em> : 10:00 – 16:00<br><em>Saturday</em> : 12:00 – 15:00<br><em>Sunday and holidays</em> : 09:00 – 12:00</div>

<div class="abs foot-title" style="left:433px;top:4845px">Useful Links</div>
<ul class="abs links" style="left:448px;top:4930px"><li>Home</li><li>Company</li><li>Projects</li><li>Contact</li></ul>
<ul class="abs links" style="left:608px;top:4930px"><li>Get A Quote</li><li>Testimonials</li><li>Construction<br>Products</li><li>Privacy Policy</li><li>Terms &amp;<br>Conditions</li></ul>

<div class="abs foot-title" style="left:834px;top:4845px">Contact Us</div>
<div class="abs contact">
  <b>Daniel R Hollis</b> | Branch Manager<br><br>
  <em>Office</em> : 555-014-2280<br>
  <em>Direct</em> : 555-017-3391<br>
  <em>Fax</em> : 555-019-6604<br>
  <em>Email</em> : dhollis@summitbuildersca.example<br><br>
  <em>Address</em> : 412 W Harbor Ridge Rd<br>
  <span style="padding-left:66px">Costa Verde, CA 92799</span>
</div>
<div class="abs copy">Copyrights © 2020 All Rights Reserved.</div>
<div class="abs socials foot-social"><span></span><span></span><span></span><span></span><span></span></div>

</body>
</html>
```